Beyond The Ledger Double Sided DL Flyer

We need a double sided flyer that we provide to a Real Estate agent for leeds. It should provide our basic services as well as a modern look and feel. The brochure should incorporate our Brand colors and have a graphic that centres around money and property. I have included a couple of pictures that we like (but have not yet purchased from PIXVAULT) as an indication of the type of picture we like.

WE need to also show the Beyond The Ledger brand and have our Phone / address's and email details.

Target Market(s)

Realestate clients (Property Investors)

Industry/Entity Type

Financial Planning

Requirements
Must have
• Picture on Front (maybe the logo on back)
• Please incorporate existing logo colours.

```html
<!DOCTYPE html>
<html lang="en">
<head>
<meta charset="utf-8">
<title>Beyond The Ledger – DL Flyer</title>
<link href="https://fonts.googleapis.com/css2?family=Open+Sans:wght@400;600;700;800&family=Oswald:wght@500&family=Roboto+Condensed:wght@400&display=swap" rel="stylesheet">
<style>
  :root{
    --brand-green:#8cc63f;
    --ink:#0d0d0d;
    --paper:#f7f7f7;
    --white:#ffffff;
    --backdrop:#d6d6d6;
  }
  *{margin:0;padding:0;box-sizing:border-box}
  html,body{width:1200px;height:1200px;overflow:hidden}
  body{background:var(--backdrop);position:relative;font-family:"Open Sans",Arial,sans-serif}

  .flyer{position:absolute;top:140px;width:478px;height:1013px;overflow:hidden;box-shadow:4px 6px 10px rgba(0,0,0,.25)}
  .flyer--front{left:99px;background:linear-gradient(180deg,var(--white) 0%,var(--paper) 60%,#ececec 100%)}
  .flyer--back{left:628px;background:var(--ink)}

  /* brand block */
  .brand{position:absolute;left:0;width:100%;display:flex;align-items:center;justify-content:center;gap:10px}
  .brand__mark{width:14px;height:14px;background:var(--brand-green)}
  .brand__name{font-weight:800;font-size:31px;line-height:1;letter-spacing:.5px;text-transform:uppercase}

  .flyer--front .brand{top:70px}
  .flyer--front .brand__name{color:var(--brand-green)}

  .hero-art{position:absolute;left:0;top:0}

  .headline{position:absolute;left:0;width:100%;text-align:center;font-weight:800;line-height:1;letter-spacing:-.5px}
  .headline--accent{top:728px;font-size:44px;color:var(--brand-green)}
  .headline--main{top:772px;font-size:46px;color:var(--ink)}

  .call-arrow{position:absolute;left:50px;top:838px}
  .call-arrow__text{position:absolute;left:68px;top:857px;font-family:"Oswald",Impact,sans-serif;font-weight:500;font-size:36px;color:var(--white);line-height:1;letter-spacing:.3px}

  .web-band{position:absolute;left:0;bottom:12px;width:100%;height:56px;display:flex;align-items:center;justify-content:center;font-size:25px;color:var(--white);letter-spacing:.3px}
  .flyer--front .web-band{background:var(--ink)}
  .flyer--back .web-band{background:var(--brand-green)}

  /* back */
  .flyer--back .brand{top:554px}
  .flyer--back .brand__name{color:var(--white)}

  .services{position:absolute;left:28px;top:637px;width:430px}
  .services__title{font-size:28px;font-weight:700;color:var(--brand-green);line-height:1}
  .services__intro{margin:12px 0 0 20px;width:372px;font-size:15.5px;font-weight:700;color:var(--brand-green);line-height:1.15;text-align:justify;text-align-last:left}
  .services__list{list-style:none;margin:8px 0 0 20px}
  .services__list li{font-family:"Roboto Condensed",Arial,sans-serif;font-size:15px;color:var(--white);line-height:25.7px;padding-left:16px;position:relative}
  .services__list li::before{content:"";position:absolute;left:2px;top:12px;width:3px;height:3px;border-radius:50%;background:var(--white)}

  .contact{position:absolute;left:30px;width:440px;color:var(--white);font-weight:700;font-size:14.5px;display:flex;align-items:center;gap:6px;white-space:nowrap}
  .contact--address{top:876px}
  .contact--lines{top:902px;justify-content:space-between}
  .contact__item{display:flex;align-items:center;gap:6px}
</style>
</head>
<body>

<section class="flyer flyer--front">
  <svg class="hero-art" width="478" height="1013" viewBox="0 0 478 1013">
    <defs>
      <radialGradient id="heroTone" cx="45%" cy="45%" r="65%">
        <stop offset="0" stop-color="#b9cf3a"/>
        <stop offset=".55" stop-color="#7f9a24"/>
        <stop offset="1" stop-color="#3e3a1c"/>
      </radialGradient>
    </defs>
    <circle cx="318" cy="432" r="288" fill="var(--brand-green)"/>
    <circle cx="322" cy="428" r="276" fill="var(--paper)"/>
    <circle cx="326" cy="424" r="268" fill="var(--ink)"/>
    <circle cx="330" cy="414" r="262" fill="url(#heroTone)" role="img" aria-label="Photo: money tree hung with dollar bags beside coin stacks and a toy house locked with a chain and padlock"/>
  </svg>
  <div class="brand">
    <span class="brand__name">Beyond The Ledger</span>
    <span class="brand__mark"></span>
  </div>

  <h1 class="headline headline--accent">LOOKING TO GROW</h1>
  <h2 class="headline headline--main">YOUR BUSINESS?</h2>

  <svg class="call-arrow" width="400" height="90" viewBox="0 0 400 90">
    <polygon points="0,15 320,15 320,0 379,36 320,74 320,57 0,57" fill="var(--brand-green)"/>
  </svg>
  <p class="call-arrow__text">CALL : (02) 5550 1824</p>

  <div class="web-band">www.beyondtheledger.com.au</div>
</section>

<section class="flyer flyer--back">
  <svg class="hero-art" width="478" height="1013" viewBox="0 0 478 1013">
    <defs>
      <radialGradient id="coinTone" cx="50%" cy="40%" r="60%">
        <stop offset="0" stop-color="#b8a07a"/>
        <stop offset=".45" stop-color="#e2b79a"/>
        <stop offset="1" stop-color="#ffffff"/>
      </radialGradient>
    </defs>
    <path d="M0,0 H478 V300 C380,440 200,500 0,470 Z" fill="url(#coinTone)" role="img" aria-label="Photo: cupped hands holding a pile of coins"/>
    <path d="M0,466 C180,500 330,460 445,330" fill="none" stroke="var(--brand-green)" stroke-width="9"/>
    <polygon points="430,320 462,292 458,336" fill="var(--brand-green)"/>
  </svg>

  <div class="brand">
    <span class="brand__name">Beyond The Ledger</span>
    <span class="brand__mark"></span>
  </div>

  <div class="services">
    <h3 class="services__title">SERVICES</h3>
    <p class="services__intro">Accountants and Financial Advisors who specialise in:</p>
    <ul class="services__list">
      <li>NEGATIVE GEARING &amp; INVESTMENT PROPERTIES</li>
      <li>PROPERTY &amp; CAPITAL GAINS TAX MINIMISATION</li>
      <li>SELF-MANAGED SUPERANNUATION FUNDS (SMSF)</li>
      <li>SMALL BUSINESS &amp; PERSONAL TAXATION</li>
      <li>INVESTMENT ADVICE &amp; RISK INSURANCES</li>
    </ul>
  </div>

  <p class="contact contact--address">
    <svg width="11" height="15" viewBox="0 0 11 15"><path d="M5.5,0 A5.5,5.5 0 0 1 11,5.5 C11,9 5.5,15 5.5,15 C5.5,15 0,9 0,5.5 A5.5,5.5 0 0 1 5.5,0 Z" fill="var(--white)"/><circle cx="5.5" cy="5.5" r="2" fill="var(--ink)"/></svg>
    Suite 8 / 41 Harbour View Road Kelston NSW 2000
  </p>
  <div class="contact contact--lines">
    <span class="contact__item">
      <svg width="11" height="13" viewBox="0 0 11 13"><path d="M2,0 L4.5,3 L3,5 C4,7.5 5.5,9 7.5,10 L9,8.5 L11,11 L9,13 C4,12 0,7 0,2 Z" fill="var(--white)"/></svg>
      (02) 5550 1824
    </span>
    <span class="contact__item">
      <svg width="16" height="12" viewBox="0 0 16 12"><rect width="16" height="12" fill="var(--white)"/><path d="M0,0 L8,7 L16,0" fill="none" stroke="var(--ink)" stroke-width="1.4"/></svg>
      hello@beyondtheledger.com.au
    </span>
  </div>

  <div class="web-band">www.beyondtheledger.com.au</div>
</section>

</body>
</html>
```